Business card for a doctor's practice

Would like a business card for a Pulmonary ( lung) doctor. I would like to include a logo with something in reference to air or oxygen or lungs. Would like the color red included somehow. Name of the company is Breathwell Medical Associates of Eastern Carolina and we specialize in Pulmonary Medicine,. I would like something streamlined and modern
Target Market(s)
Patients, hospitals, other doctors
Industry/Entity Type
Business
Contact Information for Business Card
Would like business details superimposed on a logo somehow
Look and feel

```html
<!DOCTYPE html>
<html lang="en">
<head>
<meta charset="utf-8">
<title>Breathwell Medical Associates – Business Card</title>
<link rel="stylesheet" href="https://fonts.googleapis.com/css2?family=Montserrat:wght@300;400&family=Open+Sans:wght@400;600;700&display=swap">
<style>
  :root {
    --page-bg: #e9e6e2;
    --card-black: #0d0d0e;
    --card-black-soft: #1c1c1e;
    --brand-red: #e8202a;
    --swoosh-grey: #a7a7a9;
    --text-white: #ffffff;
    --text-grey: #9b9b9d;
    --rule-grey: #8a8a8c;
  }
  * { box-sizing: border-box; margin: 0; padding: 0; }
  html, body {
    width: 1200px; height: 900px; overflow: hidden;
    background: var(--page-bg);
  }
  .sheet {
    width: 1200px; height: 900px;
    display: flex; flex-direction: column; align-items: center; justify-content: center;
    gap: 60px;
  }
  .card {
    position: relative;
    width: 640px; height: 366px;
    background: radial-gradient(ellipse at 45% 35%, var(--card-black-soft), var(--card-black) 75%);
    border-radius: 4px;
    overflow: hidden;
    box-shadow: 0 10px 28px rgba(0,0,0,.25);
  }

  /* wordmark */
  .wordmark { position: absolute; text-align: center; }
  .wordmark__name {
    font-family: "Montserrat", sans-serif; font-weight: 300;
    color: var(--brand-red); letter-spacing: 1px; line-height: 1;
    display: flex; align-items: center; justify-content: center; gap: 8px;
  }
  .wordmark__dot {
    width: .62em; height: .62em; border-radius: 50%;
    border: 2px solid var(--brand-red); display: inline-block;
  }
  .wordmark__tag {
    font-family: "Montserrat", sans-serif; font-weight: 400;
    color: var(--text-grey);
    display: flex; align-items: center; justify-content: center; gap: 10px;
    margin-top: 4px;
  }
  .wordmark__tag::before, .wordmark__tag::after {
    content: ""; height: 1px; background: var(--rule-grey); flex: 1;
  }

  .card--front .wordmark { left: 90px; right: 90px; top: 148px; }
  .card--front .wordmark__name { font-size: 38px; }
  .card--front .wordmark__tag { font-size: 17px; }

  .card--back .wordmark { left: 328px; width: 280px; top: 78px; }
  .card--back .wordmark__name { font-size: 27px; gap: 6px; }
  .card--back .wordmark__tag { font-size: 12.5px; }

  /* contact block */
  .contact {
    position: absolute; left: 44px; top: 52px;
    font-family: "Open Sans", sans-serif; color: var(--text-white);
  }
  .contact__name { color: var(--brand-red); font-weight: 700; font-size: 17px; }
  .contact__title { font-weight: 600; font-size: 13px; margin-top: 2px; }
  .contact__list { list-style: none; margin-top: 28px; font-size: 14.5px; }
  .contact__list li { display: flex; align-items: center; gap: 9px; height: 21px; }
  .contact__list svg { width: 12px; height: 12px; fill: var(--brand-red); flex: none; }
  .contact__address { margin-top: 24px; font-size: 15px; line-height: 1.5; }

  .card__wave { position: absolute; inset: 0; }
  .card__web {
    position: absolute; right: 28px; top: 236px;
    font-family: "Open Sans", sans-serif; font-size: 12.5px; color: var(--text-white);
  }
</style>
</head>
<body>
<main class="sheet">

  <section class="card card--front" aria-label="Card front">
    <div class="wordmark">
      <div class="wordmark__name"><span class="wordmark__dot"></span>BREATHWELL</div>
      <div class="wordmark__tag">Medical Associates</div>
    </div>
  </section>

  <section class="card card--back" aria-label="Card back">
    <svg class="card__wave" viewBox="0 0 640 366" preserveAspectRatio="none" aria-hidden="true">
      <path d="M0,326 C110,318 190,262 320,252 C450,242 545,196 640,176 L640,214 C545,228 450,262 330,276 C200,290 110,336 0,344 Z" fill="var(--swoosh-grey)"/>
      <path d="M0,344 C110,336 200,290 330,276 C450,262 545,228 640,214" fill="none" stroke="#000" stroke-width="4"/>
      <path d="M0,348 C110,340 200,296 330,284 C450,270 545,220 640,196 L640,366 L0,366 Z" fill="var(--brand-red)"/>
    </svg>

    <div class="contact">
      <div class="contact__name">Daniel Hartley</div>
      <div class="contact__title">Managing Director</div>
      <ul class="contact__list">
        <li><svg viewBox="0 0 12 12"><path d="M1 4 Q6 0 11 4 L9.5 5.5 L8 4.5 L8 3.5 Q6 3 4 3.5 L4 4.5 L2.5 5.5 Z M3 6 H9 L10 11 H2 Z"/></svg>(252) 555 0148</li>
        <li><svg viewBox="0 0 12 12"><path d="M3.5 0 H8.5 A1 1 0 0 1 9.5 1 V11 A1 1 0 0 1 8.5 12 H3.5 A1 1 0 0 1 2.5 11 V1 A1 1 0 0 1 3.5 0 Z M4 1.5 V9.5 H8 V1.5 Z"/></svg>(252) 555 0193</li>
        <li><svg viewBox="0 0 12 12"><path d="M0 2 H12 V10 H0 Z M1 3 L6 7 L11 3 Z" fill-rule="evenodd"/></svg>info@breathwellmed.com</li>
      </ul>
      <p class="contact__address">410 Harbor Lane, Greenville,<br>NC 27834</p>
    </div>

    <div class="wordmark">
      <div class="wordmark__name"><span class="wordmark__dot"></span>BREATHWELL</div>
      <div class="wordmark__tag">Medical Associates</div>
    </div>

    <div class="card__web">www.breathwellmed.com</div>
  </section>

</main>
</body>
</html>
```